Business Card Design

We need a business card design for a kids clothes shop in Ireland called "Tiny Trotz". Would prefer the colours Lime Green and Dark Purple to be used but are open to suggestions. The logo should include a "Cool" penguin with clothes on.

Industry/Entity Type

Shop

Contact Information for Business Card

Tiny Trotz
Harlow Arcade,
Ashvale Road, Childrenswear 0-12yrs
Millbrook,
XQ82 5LW. Deirdre Walsh.

```html
<!DOCTYPE html>
<html lang="en">
<head>
<meta charset="utf-8">
<title>Tiny Trotz – Business Card</title>
<link rel="stylesheet" href="https://fonts.googleapis.com/css2?family=Patrick+Hand&display=swap">
<style>
  :root {
    --page-bg: #c2f5a6;
    --card-green: #67bd45;
    --card-edge: #58a83a;
    --brand-purple: #8b2a9a;
    --rule-white: #ffffff;
    --mascot-dark: #3a3a3a;
    --mascot-light: #6d6d6d;
  }
  * { margin: 0; padding: 0; box-sizing: border-box; }
  html, body {
    width: 1200px;
    height: 900px;
    overflow: hidden;
    background: var(--page-bg);
  }
  .canvas {
    position: relative;
    width: 1200px;
    height: 900px;
  }
  .business-card {
    position: absolute;
    left: 180px;
    top: 210px;
    width: 840px;
    height: 480px;
    background: var(--card-green);
    border-radius: 26px;
    box-shadow: 0 3px 0 var(--card-edge);
    overflow: hidden;
    font-family: "Patrick Hand", cursive;
    color: var(--brand-purple);
  }
  .mascot-art {
    position: absolute;
    right: 30px;
    top: 20px;
    width: 300px;
    height: 190px;
  }
  .brand-name {
    position: absolute;
    left: 50px;
    top: 150px;
    font-size: 84px;
    line-height: 1;
    font-weight: 400;
    color: var(--brand-purple);
  }
  .brand-rule {
    position: absolute;
    left: 250px;
    top: 250px;
    width: 300px;
    height: 2px;
    background: var(--rule-white);
  }
  .contact-block {
    position: absolute;
    left: 290px;
    top: 278px;
    text-transform: uppercase;
    letter-spacing: 0.5px;
  }
  .contact-name {
    font-size: 34px;
    line-height: 1.1;
    margin-bottom: 10px;
  }
  .contact-line {
    font-size: 25px;
    line-height: 1.35;
  }
</style>
</head>
<body>
<main class="canvas">
  <section class="business-card">
    <svg class="mascot-art" viewBox="0 0 300 190" role="img" aria-label="Illustration of a cool penguin mascot in a dark hoodie, sunglasses and checked trainers, pointing left">
      <defs>
        <linearGradient id="mascot-tone" x1="0" y1="0" x2="1" y2="1">
          <stop offset="0" stop-color="var(--mascot-light)"/>
          <stop offset="1" stop-color="var(--mascot-dark)"/>
        </linearGradient>
      </defs>
      <rect x="0" y="0" width="300" height="190" rx="40" fill="url(#mascot-tone)"/>
    </svg>

    <h1 class="brand-name">Tiny Trotz</h1>
    <div class="brand-rule"></div>

    <address class="contact-block">
      <p class="contact-name">Deirdre Walsh</p>
      <p class="contact-line">Harlow Arcade, Ashvale Road,</p>
      <p class="contact-line">Childrenswear 0-12yrs</p>
      <p class="contact-line">Millbrook, XQ82 5LW</p>
    </address>
  </section>
</main>
</body>
</html>
```